Billboard for Lawyers who handle work accident cases

We need a billboard design for our law firm based in Queens, New York. The billboard is 8 by 10. The billboard is long and not wide.

Our firm focuses on work accidents. We are looking for a professional ad that will catch the attention of drivers and pedestrians passing by. The ad should be to the point.

I am attaching our picture and our logo for the ad. We like the idea of using the slogan "HURT AT WORK?" in English and Spanish "HERIDO EN EL TRABAJO?";

We want minimal writing on the billboard. Our telephone number should be included. The ad should say "Millions Recovered for our clients" It should also say "Attorney Advertisement" in small font in a discrete place. We would like use colors that match/coordinate the colors of our logo and/or picture but it is not required. The design should communicate serious/professional tone with a hint of modern/vibrant attorneys.

Once we have something to work with we will work with the designer for adjustments.

All people injured at work

Law Firm

• Must have HURT AT WORK and HERIDO EN EL TRABAJO (Spanish) OR another similar catchphrase
• Must have "Millions recovered for our clients"
• Must have telephone number (718) 555-0193
• Must have website "tqlegalteam.com"
• Must have in small font "Attorney Advertisement"

```html
<!DOCTYPE html>
<html lang="en">
<head>
<meta charset="utf-8">
<title>Torres &amp; Quill – Hurt at Work Billboard</title>
<link href="https://fonts.googleapis.com/css2?family=Oswald:wght@700&family=Open+Sans:ital,wght@0,400;0,700;1,400&family=Cinzel:wght@500&display=swap" rel="stylesheet">
<style>
  :root {
    --stage: #d9d9d9;
    --paper: #ffffff;
    --ink: #1c1c1c;
    --gold: #9a7b4f;
    --gold-dark: #7d6038;
    --navy: #1f2b4d;
    --navy-light: #34456f;
    --rule: #b9a27f;
  }
  html, body {
    margin: 0;
    width: 774px;
    height: 1200px;
    overflow: hidden;
    background: var(--stage);
  }
  .billboard-frame {
    position: absolute;
    left: 17px;
    top: 138px;
    width: 740px;
    height: 924px;
    box-shadow: 0 6px 18px rgba(0,0,0,.25);
  }
  .billboard {
    position: absolute;
    left: 0;
    top: 0;
    width: 565px;
    height: 705px;
    transform: scale(1.3097);
    transform-origin: 0 0;
    background: var(--paper);
    overflow: hidden;
    font-family: "Open Sans", sans-serif;
    color: var(--ink);
  }
  .backdrop { position: absolute; left: 0; top: 0; }

  .firm-name {
    position: absolute;
    top: 34px;
    left: 0;
    width: 565px;
    text-align: center;
    font-family: "Cinzel", serif;
    font-weight: 500;
    font-size: 27px;
    letter-spacing: 1px;
    color: var(--ink);
    line-height: 1;
  }
  .firm-name .firm-mark {
    display: inline-block;
    width: 12px;
    height: 12px;
    background: var(--gold);
    margin-right: 10px;
    vertical-align: 4px;
  }
  .firm-tagline {
    position: absolute;
    top: 73px;
    left: 0;
    width: 565px;
    text-align: center;
    font-family: "Cinzel", serif;
    font-size: 12px;
    letter-spacing: 1.5px;
    color: var(--ink);
  }
  .claim {
    position: absolute;
    top: 110px;
    left: 0;
    width: 565px;
    text-align: center;
    font-size: 21px;
    color: #333;
  }
  .claim strong { color: var(--gold); font-weight: 700; }

  .headline {
    position: absolute;
    left: 0;
    width: 565px;
    margin: 0;
    text-align: center;
    font-family: "Oswald", sans-serif;
    font-weight: 700;
    text-transform: uppercase;
    color: var(--ink);
    line-height: 1;
  }
  .headline-en { top: 148px; font-size: 64px; letter-spacing: -0.5px; }
  .headline-es { top: 215px; font-size: 45px; letter-spacing: -0.3px; }

  .disclaimer {
    position: absolute;
    top: 273px;
    left: 0;
    width: 565px;
    text-align: center;
    font-style: italic;
    font-size: 13px;
    color: var(--gold);
  }

  .attorney-photo {
    position: absolute;
    border-radius: 110px 110px 0 0;
  }
  .attorney-left {
    left: 55px; top: 295px; width: 260px; height: 350px;
    background: linear-gradient(180deg, #b89884 0%, #a58570 45%, var(--navy-light) 62%, var(--navy) 100%);
  }
  .attorney-right {
    left: 305px; top: 305px; width: 260px; height: 340px;
    background: linear-gradient(180deg, #b08f7b 0%, #9c7c68 45%, var(--navy-light) 64%, var(--navy) 100%);
  }

  .footer {
    position: absolute;
    left: 0;
    top: 645px;
    width: 565px;
    height: 60px;
    background: var(--paper);
    display: flex;
    align-items: center;
    justify-content: center;
    gap: 10px;
  }
  .phone {
    display: flex;
    align-items: center;
    gap: 6px;
    font-family: "Oswald", sans-serif;
    font-weight: 700;
    font-size: 29px;
    color: var(--ink);
  }
  .divider { width: 2px; height: 30px; background: var(--gold); }
  .website {
    display: flex;
    align-items: center;
    gap: 5px;
    font-size: 17px;
    color: var(--ink);
  }
  .website strong { color: var(--gold); font-weight: 700; }
</style>
</head>
<body>
<div class="billboard-frame">
  <div class="billboard">
    <svg class="backdrop" width="565" height="705" viewBox="0 0 565 705" aria-hidden="true">
      <line x1="98" y1="140" x2="465" y2="140" stroke="var(--rule)" stroke-width="1"/>
      <polygon points="276,140 294,140 285,149" fill="var(--gold)"/>
      <line x1="95" y1="282" x2="195" y2="282" stroke="var(--rule)" stroke-width="1"/>
      <line x1="362" y1="282" x2="462" y2="282" stroke="var(--rule)" stroke-width="1"/>
      <polygon points="0,265 470,545 470,645 0,645" fill="var(--ink)"/>
      <polygon points="565,255 285,418 565,585" fill="var(--gold)"/>
    </svg>

    <div class="firm-name"><span class="firm-mark"></span>Torres &amp; Quill</div>
    <div class="firm-tagline">ATTORNEYS AT LAW</div>

    <p class="claim" style="margin:0">Millions Recovered For <strong>Our Clients</strong></p>

    <h1 class="headline headline-en">Hurt at Work</h1>
    <h2 class="headline headline-es">Herido en el Trabajo</h2>

    <div class="disclaimer">Attorney Advertisement</div>

    <div class="attorney-photo attorney-left" role="img" aria-label="Portrait photo of the first attorney in a navy suit and blue tie"></div>
    <div class="attorney-photo attorney-right" role="img" aria-label="Portrait photo of the second attorney in a navy suit and red tie"></div>

    <div class="footer">
      <div class="phone">
        <svg width="22" height="22" viewBox="0 0 24 24" aria-hidden="true">
          <circle cx="12" cy="12" r="10.5" fill="none" stroke="var(--gold)" stroke-width="1.6"/>
          <path d="M8.3 6.8c.4-.4 1-.4 1.3 0l1.3 1.6c.3.4.3.9-.1 1.3l-.7.7c.6 1.3 1.6 2.3 2.9 2.9l.7-.7c.4-.4.9-.4 1.3-.1l1.6 1.3c.4.3.4.9 0 1.3l-.9.9c-.7.7-1.8.8-2.7.3-2.2-1.2-4-3-5.2-5.2-.5-.9-.4-2 .3-2.7z" fill="var(--gold)"/>
        </svg>
        (718) 555-0193
      </div>
      <div class="divider"></div>
      <div class="website">
        <svg width="13" height="13" viewBox="0 0 24 24" aria-hidden="true">
          <g fill="none" stroke="var(--gold)" stroke-width="2">
            <circle cx="12" cy="12" r="10"/>
            <ellipse cx="12" cy="12" rx="4.5" ry="10"/>
            <line x1="2" y1="12" x2="22" y2="12"/>
          </g>
        </svg>
        <span>www.<strong>tqlegalteam</strong>.com</span>
      </div>
    </div>
  </div>
</div>
</body>
</html>
```